RW Hornets Dalby (Social Media Pack & Stationary)

Create Stationary Designs as well as Social Media Designs (Twitter, Instagram & Facebook) as well as a Square and Banner Social media template... keep the logo I attached in the Ai file... I would like the blue in the RW Hornets logo to be navy blue instead of the dark blue.

Willing to give a good tip to get it done quicker

Please use the logo provided in the ai file.

Instagram account: @rwhdalby
FB account: RW Hornets Dalby
Twitter: @rwhdalby

Parents and players

Serif

0255a3
f78f20
f37122

• Stationary
Twitter & FB heading
Template to post social media announcements
Template for pictures to post on social media
Template to post schedule
Envelop
Business Card
(All must include logo)

```html
<!DOCTYPE html>
<html lang="en">
<head>
<meta charset="utf-8">
<title>RW Hornets Dalby – Envelope</title>
<link rel="stylesheet" href="https://fonts.googleapis.com/css2?family=Roboto:wght@400;700&display=swap">
<style>
  :root {
    --navy: #0f1147;
    --paper: #ffffff;
    --backdrop: #ecebea;
    --ink: #474747;
    --rule: #555555;
  }
  * { margin: 0; padding: 0; box-sizing: border-box; }
  html, body {
    width: 1200px; height: 800px; overflow: hidden;
    background: var(--backdrop);
    font-family: "Roboto", Arial, sans-serif;
  }
  .canvas { position: relative; width: 1200px; height: 800px; }

  .envelope {
    position: absolute;
    width: 740px; height: 322px;
    background: var(--paper);
    box-shadow: 0 2px 6px rgba(0,0,0,0.12);
    overflow: hidden;
  }
  .envelope-back { left: 400px; top: 40px; }
  .envelope-front { left: 80px; top: 438px; }

  .flap { position: absolute; left: 0; top: 0; width: 740px; height: 70px; }

  .sender {
    position: absolute; left: 38px; top: 36px;
    display: flex; align-items: center;
  }
  .sender-name {
    font-weight: 700; font-size: 30px; line-height: 1;
    color: var(--navy); padding-right: 18px;
  }
  .divider { width: 1px; height: 74px; background: var(--rule); margin-right: 14px; }
  .contact-list { list-style: none; font-size: 11.5px; color: var(--ink); line-height: 15px; }
  .contact-item { display: flex; align-items: center; gap: 6px; }
  .contact-icon { width: 9px; height: 9px; flex: none; }
  .contact-square { width: 8px; height: 8px; background: var(--navy); border-radius: 1px; flex: none; }

  .footer-band {
    position: absolute; left: 0; right: 0; bottom: 8px;
    height: 12px; background: var(--navy);
  }
</style>
</head>
<body>
<main class="canvas">

  <section class="envelope envelope-back" aria-label="Envelope back with navy flap">
    <svg class="flap" viewBox="0 0 740 70" aria-hidden="true">
      <path d="M0 0 H740 V30 Q740 40 730 46 L700 66 Q694 70 684 70 H56 Q46 70 40 66 L10 46 Q0 40 0 30 Z" fill="var(--navy)"/>
    </svg>
  </section>

  <section class="envelope envelope-front" aria-label="Envelope front">
    <div class="sender">
      <div class="sender-name">RW Hornets</div>
      <div class="divider"></div>
      <ul class="contact-list">
        <li class="contact-item">
          <svg class="contact-icon" viewBox="0 0 10 10" aria-hidden="true"><path d="M2 1 L4 1 L4.6 3.2 L3.4 4 Q4.4 6 6 6.6 L6.8 5.4 L9 6 L9 8 Q9 9 8 9 Q1 8.6 1 2 Q1 1 2 1 Z" fill="var(--navy)"/></svg>
          <span>555.014.2736</span>
        </li>
        <li class="contact-item">
          <svg class="contact-icon" viewBox="0 0 10 10" aria-hidden="true"><rect x="0.5" y="2" width="9" height="6.5" fill="var(--navy)"/><path d="M0.5 2 L5 5.8 L9.5 2" stroke="#fff" stroke-width="0.9" fill="none"/></svg>
          <span>coach@rwhornetsmail.com</span>
        </li>
        <li class="contact-item"><span class="contact-square"></span><span>RW Hornets Dalby</span></li>
        <li class="contact-item"><span class="contact-square"></span><span>@rwhdalby</span></li>
        <li class="contact-item"><span class="contact-square"></span><span>@rwhdalby</span></li>
      </ul>
    </div>
    <div class="footer-band"></div>
  </section>

</main>
</body>
</html>
```